Vorlan cards

I am in the auto motive, transportation business I would like a business card that is Something cool, modern edgy, having to do with car culture. I offer towing service for high and exotic cars. I also provide towing for collisions and car accidents. I offer open and enclosed transport nationwide.

Target Market(s)

Car culture people high end auto collectors

Industry/Entity Type

Towing car carrier

Contact Information for Business Card

My company colors black yellow and silver

Font styles to use
Serif

```html
<!DOCTYPE html>
<html lang="en">
<head>
<meta charset="utf-8">
<title>Vorlan Transportation – Business Cards</title>
<link rel="stylesheet" href="https://fonts.googleapis.com/css2?family=Roboto+Slab:wght@400;700&display=swap">
<style>
  :root {
    --backdrop: #2a2a2a;
    --card: #1d1d1d;
    --pattern-light: #262626;
    --pattern-dark: #161616;
    --yellow: #f2d33a;
    --silver: #c9c9c9;
    --white: #f4f4f4;
  }
  * { box-sizing: border-box; margin: 0; padding: 0; }
  html, body {
    width: 1200px; height: 900px; overflow: hidden;
    background: var(--backdrop);
    font-family: "Roboto Slab", Georgia, serif;
  }
  .stage {
    width: 1200px; height: 900px;
    display: flex; flex-direction: column;
    align-items: center; justify-content: center; gap: 30px;
  }
  .card {
    position: relative;
    width: 700px; height: 400px;
    background: var(--card);
    border-radius: 20px;
    box-shadow: 0 16px 40px rgba(0,0,0,.45);
    color: var(--white);
    overflow: hidden;
  }

  /* Front */
  .identity { position: absolute; left: 70px; top: 92px; }
  .identity .name {
    color: var(--yellow); font-weight: 700;
    font-size: 30px; line-height: 36px; letter-spacing: .5px; text-transform: uppercase;
  }
  .identity .role { font-size: 17px; line-height: 22px; margin-top: 4px; }
  .divider {
    position: absolute; left: 70px; right: 60px; top: 178px;
    height: 2px; background: var(--yellow);
  }
  .contacts { position: absolute; left: 70px; top: 200px; list-style: none; }
  .contacts li {
    display: flex; align-items: center; gap: 12px;
    font-size: 17px; line-height: 32px;
  }
  .contacts svg { width: 16px; height: 16px; flex: none; }
  .brand {
    position: absolute; display: flex; align-items: center; gap: 10px;
  }
  .card-front .brand { right: 60px; top: 96px; }
  .brand .mark { width: 22px; height: 22px; border-radius: 50%; background: var(--yellow); }
  .brand .wordmark {
    color: var(--silver); font-weight: 700; font-size: 40px; line-height: 48px; letter-spacing: 2px;
  }
  .address {
    position: absolute; right: 60px; bottom: 46px;
    text-align: right; font-size: 17px; line-height: 26px; font-style: normal;
  }

  /* Back */
  .pattern-field {
    position: absolute; inset: 0;
    background: linear-gradient(135deg, var(--pattern-light) 0%, var(--pattern-dark) 55%, var(--pattern-light) 100%);
  }
  .card-back .brand { left: 70px; top: 70px; }
  .card-back .brand .wordmark { font-size: 32px; line-height: 40px; }
  .card-back .brand .mark { width: 18px; height: 18px; }
</style>
</head>
<body>
<main class="stage">
  <section class="card card-front">
    <header class="identity">
      <h1 class="name">Dorian Vale</h1>
      <p class="role">CEO/Founder</p>
    </header>

    <div class="brand">
      <span class="mark"></span>
      <span class="wordmark">VORLAN</span>
    </div>

    <div class="divider"></div>

    <ul class="contacts">
      <li>
        <svg viewBox="0 0 24 24" aria-hidden="true"><path fill="var(--yellow)" d="M6.6 10.8a15 15 0 0 0 6.6 6.6l2.2-2.2a1 1 0 0 1 1-.25 11.4 11.4 0 0 0 3.6.57 1 1 0 0 1 1 1V20a1 1 0 0 1-1 1A17 17 0 0 1 3 4a1 1 0 0 1 1-1h3.5a1 1 0 0 1 1 1c0 1.25.2 2.45.57 3.57a1 1 0 0 1-.25 1z"/></svg>
        (555) 210 4470
      </li>
      <li>
        <svg viewBox="0 0 24 24" aria-hidden="true"><rect x="6" y="2" width="12" height="20" rx="2" fill="none" stroke="var(--yellow)" stroke-width="2"/><circle cx="12" cy="18" r="1.2" fill="var(--yellow)"/></svg>
        (555) 318 9062
      </li>
      <li>
        <svg viewBox="0 0 24 24" aria-hidden="true"><rect x="2" y="5" width="20" height="14" rx="1.5" fill="var(--yellow)"/><path d="M2.5 6l9.5 7 9.5-7" fill="none" stroke="var(--card)" stroke-width="1.6"/></svg>
        info@vorlantransport.com
      </li>
      <li>
        <svg viewBox="0 0 24 24" aria-hidden="true"><circle cx="12" cy="12" r="9.5" fill="none" stroke="var(--yellow)" stroke-width="2"/><path d="M2.5 12h19M12 2.5c3 3 3 16 0 19M12 2.5c-3 3-3 16 0 19" fill="none" stroke="var(--yellow)" stroke-width="1.5"/></svg>
        www.vorlantransport.com
      </li>
    </ul>

    <address class="address">
      P.O. Box 3170 Ridge Road<br>
      Northvale AB 6021
    </address>
  </section>

  <section class="card card-back">
    <div class="pattern-field" role="img" aria-label="Repeating tone-on-tone brand emblem pattern in dark grey across the card back"></div>
    <div class="brand">
      <span class="mark"></span>
      <span class="wordmark">VORLAN</span>
    </div>
  </section>
</main>
</body>
</html>
```